Pemberly & Associates Tax Services

Need an eye catching advertisement/lead generating design for prospects interesting in professional tax planning and tax preparation services. Ideas for
Sample Advertising Language is below:

We are accepting new clients!!
We are affordable and have over 20 years of experience serving the tax needs of our clientele.

Here are a few reasons you may want to contact us:

1. You want to learn how to maximize business deductions
2. You’re a high-income earner and want to learn ways to pay less in taxes
3. You have an interest in starting a business
4. You want to maximize rental property deductions
5. You have questions about maintaining a home office
6. You want to be updated periodically on tax law changes and tax planning strategies
7. You want to be represented by a tax expert before the IRS if you are subject to an audit

References available upon request.

Target Market(s)

Individuals, small businesses and startup business

Industry/Entity Type

Tax and Accounting Industry

Requirements
Nice to have
• Would like to develop a marketing campaign that can be used periodically to digitally generate leads, build email contact list of prospective clients who want to receive tax updates.

```html
<!DOCTYPE html>
<html lang="en">
<head>
<meta charset="utf-8">
<title>Pemberly &amp; Associates Tax Services – Flyer</title>
<link href="https://fonts.googleapis.com/css2?family=Fjalla+One&family=Raleway:wght@500;600;700;800&display=swap" rel="stylesheet">
<style>
  :root {
    --navy: #13305e;
    --navy-deep: #0c2147;
    --navy-light: #1d4f8c;
    --green: #2e9e35;
    --green-bright: #5cbc2b;
    --green-dark: #1b7d2a;
    --lime: #c8e02e;
    --white: #ffffff;
    --backdrop: #565656;
    --grey: #8a8f96;
  }
  * { margin: 0; padding: 0; box-sizing: border-box; }
  html, body { width: 1200px; height: 1000px; overflow: hidden; }
  body { background: var(--backdrop); font-family: "Raleway", sans-serif; position: relative; }

  .flyer {
    position: absolute; left: 270px; top: 35px; width: 652px; height: 920px;
    background: var(--white); overflow: hidden;
  }
  .flyer-shapes { position: absolute; inset: 0; }

  .brand { position: absolute; left: 33px; top: 40px; display: flex; align-items: center; gap: 14px; }
  .brand-dot { width: 58px; height: 58px; border-radius: 50%; background: var(--white); flex: none; }
  .brand-name { color: var(--white); font-weight: 700; font-size: 24px; line-height: 25px; letter-spacing: .5px; }
  .brand-tagline { position: absolute; left: 105px; top: 100px; color: var(--green-bright); font-weight: 600; font-size: 14px; letter-spacing: .5px; }

  .headline { position: absolute; left: 43px; top: 142px; font-family: "Fjalla One", sans-serif; text-transform: uppercase; }
  .headline-main { color: var(--white); font-size: 56px; line-height: 54px; }
  .headline-accent { color: var(--green-bright); font-size: 42px; line-height: 50px; }

  .intro { position: absolute; left: 43px; top: 309px; width: 262px; color: var(--white); font-weight: 700; font-size: 17px; line-height: 19px; }

  .reasons { position: absolute; left: 15px; top: 465px; width: 343px; height: 378px; border-radius: 10px;
    background: linear-gradient(180deg, var(--navy) 0%, var(--navy-light) 55%, var(--navy) 100%); }
  .reasons-title { position: absolute; left: 24px; top: 10px; color: var(--lime); font-family: "Fjalla One", sans-serif; font-size: 21px; line-height: 27px; text-transform: uppercase; }
  .reason-list { list-style: none; position: absolute; left: 0; top: 0; }
  .reason { position: absolute; left: 0; width: 343px; }
  .reason-num { position: absolute; left: 25px; top: 0; width: 24px; height: 24px; border-radius: 50%;
    background: var(--green); border: 2px solid var(--white); color: var(--white);
    font-size: 11px; font-weight: 800; display: flex; align-items: center; justify-content: center; }
  .reason-text { position: absolute; left: 61px; top: -2px; width: 270px; color: var(--white); font-weight: 600; font-size: 13px; line-height: 14px; }

  .photo-ring { position: absolute; left: 310px; top: 44px; width: 434px; height: 434px; border-radius: 50%; background: var(--green-bright); }
  .photo-team { position: absolute; left: 328px; top: 40px; width: 430px; height: 430px; border-radius: 50%;
    background: radial-gradient(circle at 55% 40%, #f4f7fa 0%, #dde4ea 45%, #aab3bd 100%);
    border: 4px solid var(--white); }
  .photo-portrait { position: absolute; left: 404px; top: 444px; width: 176px; height: 176px; border-radius: 50%;
    background: radial-gradient(circle at 50% 40%, #b98b6c 0%, #6a4a38 55%, #2b2d3a 100%);
    border: 5px solid var(--white); box-shadow: 0 0 0 6px var(--green-bright); }

  .references { position: absolute; left: 385px; top: 645px; color: var(--green-dark); font-family: "Fjalla One", sans-serif;
    font-size: 27px; line-height: 35px; text-transform: uppercase; }
  .website { position: absolute; left: 387px; top: 725px; width: 223px; height: 32px; background: var(--navy);
    color: var(--white); font-family: "Fjalla One", sans-serif; font-size: 17px; line-height: 32px; text-align: center; }
  .website span { color: var(--lime); }
  .credential { position: absolute; left: 386px; top: 771px; width: 224px; height: 72px; border: 2px solid var(--green-bright);
    border-radius: 7px; background: var(--white); display: flex; align-items: center; padding-left: 12px; gap: 10px; }
  .credential-mark { width: 80px; height: 46px; border: 4px solid var(--grey); border-radius: 2px; }
  .credential-bar { width: 100px; height: 42px; background: #e9ecef; }

  .footer { position: absolute; left: 0; top: 853px; width: 652px; height: 67px;
    background: linear-gradient(180deg, var(--green) 0%, var(--green-dark) 100%);
    display: flex; align-items: center; color: var(--white); font-weight: 700; font-size: 12px; white-space: nowrap; }
  .footer-block { display: flex; flex-direction: column; gap: 4px; }
  .footer-brand { padding-left: 39px; width: 222px; }
  .footer-brand strong { color: var(--lime); font-weight: 800; font-size: 13.5px; }
  .footer-divider { width: 2px; height: 38px; background: var(--lime); flex: none; }
  .footer-contact { padding-left: 10px; width: 172px; }
  .footer-address { padding-left: 10px; }
  .footer-line { display: flex; align-items: center; gap: 6px; }
  .footer-line svg { flex: none; }
  .footer-indent { padding-left: 17px; }
</style>
</head>
<body>
<main class="flyer">
  <svg class="flyer-shapes" viewBox="0 0 652 920" width="652" height="920" aria-hidden="true">
    <defs>
      <linearGradient id="navyFade" x1="0" y1="0" x2="0" y2="1">
        <stop offset="0" stop-color="#0f2a55"/>
        <stop offset="1" stop-color="#0a1e3f"/>
      </linearGradient>
    </defs>
    <path d="M0 0 H652 V420 C560 432 440 398 320 408 C200 420 90 462 0 480 Z" fill="url(#navyFade)"/>
    <path d="M0 480 C120 452 260 390 380 440 C440 465 470 490 520 505 C570 520 620 510 652 500 V520 C610 532 560 540 500 525 C450 512 410 480 360 455 C260 410 120 470 0 500 Z" fill="var(--green-bright)"/>
    <path d="M500 525 C560 540 610 532 652 520 V528 C610 542 560 548 500 534 Z" fill="var(--navy)"/>
  </svg>

  <div class="photo-ring" aria-hidden="true"></div>
  <div class="photo-team" role="img" aria-label="Photo of a team of tax advisers meeting around a conference table in a bright office"></div>

  <div class="brand">
    <span class="brand-dot"></span>
    <span class="brand-name">Pemberly &amp;<br>Associates LLC</span>
  </div>
  <p class="brand-tagline">Tax &amp; Business Services</p>

  <h1 class="headline">
    <span class="headline-main">We are<br>accepting</span><br>
    <span class="headline-accent">New clients!!</span>
  </h1>
  <p class="intro">We are affordable and have over 20 years of experience serving the tax needs of our clientele.</p>

  <section class="reasons">
    <h2 class="reasons-title">Here are a few reasons you<br>may want to contact us:</h2>
    <ol class="reason-list">
      <li class="reason" style="top:83px"><span class="reason-num">1</span><span class="reason-text">You want to learn how to maximize<br>business deductions</span></li>
      <li class="reason" style="top:126px"><span class="reason-num">2</span><span class="reason-text">You’re a high-income earner and want to<br>learn ways to pay less in taxes</span></li>
      <li class="reason" style="top:166px"><span class="reason-num">3</span><span class="reason-text">You have an interest in starting a business</span></li>
      <li class="reason" style="top:200px"><span class="reason-num">4</span><span class="reason-text">You want to maximize rental<br>property deductions</span></li>
      <li class="reason" style="top:245px"><span class="reason-num">5</span><span class="reason-text">You have questions about maintaining<br>a home office</span></li>
      <li class="reason" style="top:290px"><span class="reason-num">6</span><span class="reason-text">You want to be updated periodically on tax<br>law changes and tax planning strategies</span></li>
      <li class="reason" style="top:334px"><span class="reason-num">7</span><span class="reason-text">You want to be represented by a tax expert<br>before the IRS if you are subject to an audit</span></li>
    </ol>
  </section>

  <div class="photo-portrait" role="img" aria-label="Portrait photo of the firm's lead tax adviser in a dark suit"></div>

  <p class="references">References available<br>upon request.</p>
  <p class="website">WWW.<span>PEMBERLYTAXHELP</span>.COM</p>
  <div class="credential" role="img" aria-label="Professional credential badge">
    <span class="credential-mark"></span>
    <span class="credential-bar"></span>
  </div>

  <footer class="footer">
    <div class="footer-block footer-brand">
      <strong>PEMBERLY &amp; ASSOCIATES</strong>
      <span>TAX AND BUSINESS SERVICES</span>
    </div>
    <span class="footer-divider"></span>
    <div class="footer-block footer-contact">
      <span class="footer-line">
        <svg width="12" height="12" viewBox="0 0 24 24"><path d="M6.6 10.8a15.1 15.1 0 0 0 6.6 6.6l2.2-2.2c.3-.3.7-.4 1-.2 1.1.4 2.3.6 3.6.6.6 0 1 .4 1 1V20c0 .6-.4 1-1 1A17 17 0 0 1 3 4c0-.6.4-1 1-1h3.5c.6 0 1 .4 1 1 0 1.3.2 2.5.6 3.6.1.3 0 .7-.2 1z" fill="var(--lime)"/></svg>
        (555) 214-8630
      </span>
      <span class="footer-line">
        <svg width="12" height="10" viewBox="0 0 24 18"><rect x="1" y="1" width="22" height="16" rx="2" fill="var(--lime)"/><path d="M2 2 L12 10 L22 2" stroke="var(--green-dark)" stroke-width="2" fill="none"/></svg>
        info@pemberlytax.com
      </span>
    </div>
    <span class="footer-divider"></span>
    <div class="footer-block footer-address">
      <span class="footer-line">
        <svg width="11" height="14" viewBox="0 0 20 26"><path d="M10 0a10 10 0 0 0-10 10c0 7.5 10 16 10 16s10-8.5 10-16A10 10 0 0 0 10 0z" fill="var(--lime)"/><circle cx="10" cy="10" r="3.5" fill="var(--green-dark)"/></svg>
        412 Harbor Lane, Suite 210
      </span>
      <span class="footer-indent">Lakeview, FL 34000-1200</span>
    </div>
  </footer>
</main>
</body>
</html>
```